Packaging design coffee brand

Creating a packaging design for coffee products. an existing brand shall be repositioned, complete redesign. capsules, beans, etc. We need a label for the coffee whole bean package, a folded packaging for coffee capsules, see attachment. The package for the whole bean also shall be changed into a full printed packaging.

The logo is already created, but you can play with the elements, the position of symbol and name.

Target Market(s)

Europe

Industry/Entity Type

coffee

Font styles to use
Sans Serif

Requirements
Must have
• we already have a logo, which shall be used. Position of the symbol and name can be adjusted.
Nice to have
• please see the briefing attached, there you find al relevant information.
Should not have
• shall not be ecological, it shal be a lifestyle brand.

```html
<!DOCTYPE html>
<html lang="en">
<head>
<meta charset="utf-8">
<title>Noro Kafa – Whole Bean Coffee Pouch</title>
<link href="https://fonts.googleapis.com/css2?family=Ubuntu:wght@400;500&family=Open+Sans:wght@400;600&family=Archivo+Narrow:wght@400;700&display=swap" rel="stylesheet">
<style>
  :root {
    --stage: #a8b3b1;
    --pouch: #f4f4f3;
    --pouch-seal: #ececeb;
    --ink: #2e2e2e;
    --ink-soft: #4a4a4a;
    --rule: #3a3a3a;
    --band: #1f1f20;
    --band-edge: #8e8e8e;
    --bean-dark: #3e1c12;
    --bean-mid: #7a3a26;
    --bean-light: #9c5a40;
    --white: #ffffff;
  }
  * { margin: 0; padding: 0; box-sizing: border-box; }
  html, body { width: 1200px; height: 800px; overflow: hidden; }
  body { background: var(--stage); position: relative; font-family: "Open Sans", sans-serif; color: var(--ink); }

  .pouch {
    position: absolute; top: 134px; width: 332px; height: 546px;
    background: var(--pouch); border-radius: 6px; overflow: hidden;
  }
  .pouch::before {
    content: ""; position: absolute; left: 0; right: 0; top: 0; height: 98px;
    background: var(--pouch-seal);
  }
  .pouch--front { left: 178px; }
  .pouch--back { left: 636px; }

  .brand-name {
    position: absolute; left: 0; right: 0; text-align: center;
    font-family: "Ubuntu", sans-serif; font-weight: 400; color: var(--ink-soft);
    letter-spacing: 1.5px; white-space: nowrap; line-height: 1;
  }
  .pouch--front .brand-name { top: 238px; font-size: 40px; }
  .pouch--back .brand-name { top: 220px; font-size: 30px; }

  .claim {
    position: absolute; left: 0; right: 0; text-align: center;
    font-family: "Open Sans", sans-serif; color: var(--ink); white-space: nowrap;
    font-size: 13.5px; line-height: 18px;
  }
  .claim--product { top: 283px; }
  .claim-rule { position: absolute; top: 303px; left: 92px; right: 92px; height: 1px; background: var(--rule); }
  .claim--certified { top: 305px; }

  .front-art { position: absolute; left: 0; top: 0; width: 332px; height: 546px; }
  .net-weight {
    position: absolute; left: 0; right: 0; top: 500px; text-align: center;
    font-size: 10px; color: var(--white);
  }

  .story {
    position: absolute; left: 40px; top: 266px; width: 138px;
    font-size: 8.6px; line-height: 12px; text-align: justify; text-align-last: center;
  }
  .story--short { top: 480px; left: 57px; width: 118px; font-size: 7.4px; line-height: 10px; text-align: left; text-align-last: left; }

  .nutrition {
    position: absolute; left: 184px; top: 264px; width: 107px; height: 196px;
    border: 1px solid var(--ink); padding: 2px 3px;
    font-family: "Archivo Narrow", sans-serif; font-size: 5px; line-height: 7px; color: var(--ink);
    background: var(--white);
  }
  .nutrition__title { font-weight: 700; font-size: 13px; line-height: 14px; border-bottom: 1px solid var(--ink); }
  .nutrition__serving { display: flex; justify-content: space-between; font-weight: 700; border-bottom: 3px solid var(--ink); padding-bottom: 1px; }
  .nutrition__calories { display: flex; justify-content: space-between; align-items: flex-end; font-weight: 700; font-size: 10px; line-height: 12px; border-bottom: 2px solid var(--ink); }
  .nutrition__calories span:last-child { font-size: 13px; }
  .nutrition__dv { text-align: right; border-bottom: 1px solid var(--ink); }
  .nutrition__row { display: flex; justify-content: space-between; border-bottom: 0.5px solid var(--ink); }
  .nutrition__row--sub { padding-left: 6px; }
  .nutrition__row--subsub { padding-left: 12px; }
  .nutrition__row b { font-weight: 700; }

  .code-panel { position: absolute; left: 194px; top: 470px; width: 87px; height: 64px; background: var(--band); }
</style>
</head>
<body>

<section class="pouch pouch--front" aria-label="Front of whole bean pouch">
  <svg class="front-art" viewBox="0 0 332 546">
    <defs>
      <linearGradient id="beanTone" x1="0" y1="0" x2="1" y2="1">
        <stop offset="0" stop-color="var(--bean-light)"/>
        <stop offset="0.5" stop-color="var(--bean-mid)"/>
        <stop offset="1" stop-color="var(--bean-dark)"/>
      </linearGradient>
    </defs>
    <path class="dark-band" d="M0,350 L332,342 L332,546 L0,546 Z" fill="var(--band)"/>
    <path role="img" aria-label="Photograph of roasted coffee beans"
          d="M0,352 C90,336 180,372 332,340 L332,392 C300,400 260,380 230,372 C200,366 190,384 218,388 C170,420 110,446 0,444 Z"
          fill="url(#beanTone)" stroke="var(--band-edge)" stroke-width="3"/>
  </svg>
  <div class="brand-name">NORO KAFA</div>
  <div class="claim claim--product">WHOLE BEAN COFFEE</div>
  <div class="claim-rule"></div>
  <div class="claim claim--certified">ORGANIC AND FAIR TRADE CERTIFIED</div>
  <div class="net-weight">12OZ (340g)</div>
</section>

<section class="pouch pouch--back" aria-label="Back of whole bean pouch">
  <div class="brand-name">NORO KAFA</div>
  <p class="story">Lorem ipsum dolor sit amet, consectetuer adipiscing elit, sed diam nonummy nibh euismod tincidunt ut laoreet dolore magna aliquam erat volutpat. Ut wisi enim ad minim veniam, quis nostrud exerci tation ullamcorper suscipit lobortis nisl ut aliquip ex ea commodo consequat. Duis autem vel eum iriure dolor in hendre Lorem ipsum dolor sit amet, consectetuer ullamcorper suscipit lobortis nisl ut aliquip ex ea commodo consequat. Duis autem vel eum iriure dolor in hendre</p>
  <p class="story story--short">Lorem ipsum dolor sit amet, consectetuer adipiscing elit, sed diam nonummy nibh euismod</p>

  <div class="nutrition">
    <div class="nutrition__title">Nutrition Facts</div>
    <div>10 servings per container</div>
    <div class="nutrition__serving"><span>Serving size</span><span>1 cup (55g)</span></div>
    <div><b>Amount per serving</b></div>
    <div class="nutrition__calories"><span>Calories</span><span>165</span></div>
    <div class="nutrition__dv">% Daily Value*</div>
    <div class="nutrition__row"><span><b>Total Fat</b> 1.5g</span><b>2%</b></div>
    <div class="nutrition__row nutrition__row--sub"><span>Saturated Fat 0.5g</span><b>3%</b></div>
    <div class="nutrition__row nutrition__row--sub"><span><i>Trans</i> Fat 0g</span><span></span></div>
    <div class="nutrition__row nutrition__row--sub"><span>Polyunsaturated Fat 0.5g</span><span></span></div>
    <div class="nutrition__row nutrition__row--sub"><span>Monounsaturated Fat 0.5g</span><span></span></div>
    <div class="nutrition__row"><span><b>Cholesterol</b> 0mg</span><b>0%</b></div>
    <div class="nutrition__row"><span><b>Sodium</b> 180mg</span><b>8%</b></div>
    <div class="nutrition__row"><span><b>Fluoride</b> 0g</span><span></span></div>
    <div class="nutrition__row"><span><b>Total Carbohydrate</b> 21g</span><b>8%</b></div>
    <div class="nutrition__row nutrition__row--sub"><span>Dietary Fiber 2g</span><b>7%</b></div>
    <div class="nutrition__row nutrition__row--subsub"><span>Soluble Fiber &lt;1g</span><span></span></div>
    <div class="nutrition__row nutrition__row--subsub"><span>Insoluble Fiber 1g</span><span></span></div>
    <div class="nutrition__row nutrition__row--sub"><span>Total Sugars 8g</span><span></span></div>
    <div class="nutrition__row nutrition__row--subsub"><span>Includes 6g Added Sugars</span><b>12%</b></div>
  </div>

  <div class="code-panel"></div>
</section>

</body>
</html>
```